Flyer-Design für Wohn -und Einrichtungsberaterin
Zielgruppe
Ich bin eine Wohn -und Einrichtungsberaterin und biete neben der Wohnraumopitimierung auch Gartenberatung und Workshops an. Ich bin gelernte Floristin und habe daher einen engen Bezug zur Natürlichkeit.
Aufgabenstellung
Mein Flyer soll die Größe 148 x 148mm haben, mit einer klaren und ruhigen Erscheinung. Das Farbkonzept sollte sich in natürlichen und gedeckten Erdtönen wiederfinden. Trotzdem soll das Konzept ausdrucksstark präsentiert werden.
Vorderseite:
-transparentes Wohnbild im Hintergrund, darauf das Logo
-Bild (Tisch) und Logo siehe Anhänge
Rückseite:
-4 quadratische Textwürfel 2x2 angeordnet (neben- und untereinander)
1. Würfel (oben links)
Überschrift: WOHNRAUMGESTALTUNG
Text: Mit der vorhandenen Einrichtung eine Verbesserung des Wohngefühls schaffen.
2. Würfel (oben rechts)
Überschrift:GARTENBERATUNG
Text: Durch Anregung in der Garten -und Terassengestaltung ein neues Erscheinungsbild kreieren.
3. Würfel (unten links)
Überschrift: RAUMDESIGN
Text: In Praxis- und Gewerberäumen eine neue Atmosphäre erzielen.
4.Würfel (unten rechts)
Überschrift: WORKSHOPS
Text: Kreative Gruppenevents zu verschiedensten Anlässen und Themen erleben.

```html
<!DOCTYPE html>
<html lang="de">
<head>
<meta charset="utf-8">
<title>Heimklang – Flyer</title>
<link rel="stylesheet" href="https://fonts.googleapis.com/css2?family=EB+Garamond:wght@400&family=Jost:wght@300;400&display=swap">
<style>
  :root {
    --paper: #ffffff;
    --ink-heading: #3a3a3c;
    --ink-body: #6f6358;
    --ink-logo: #3b4441;
    --frame: rgba(255,255,255,0.9);
    --photo-front-a: #c9c3b6;
    --photo-front-b: #b9a794;
    --photo-front-c: #d8d3c9;
    --photo-back-a: #cfc6bd;
    --photo-back-b: #bcaea2;
    --photo-back-c: #d9d2ca;
  }
  * { margin: 0; padding: 0; box-sizing: border-box; }
  html, body { width: 1200px; height: 653px; overflow: hidden; background: var(--paper); }
  .canvas { position: relative; width: 1200px; height: 653px; }

  .flyer-side { position: absolute; top: 104px; width: 479px; height: 478px; overflow: hidden; }
  .flyer-front { left: 112px; }
  .flyer-back { left: 604px; }

  .photo { position: absolute; inset: 0; }
  .photo-front {
    background:
      radial-gradient(ellipse at 70% 20%, rgba(140,175,165,0.55), transparent 45%),
      linear-gradient(180deg, var(--photo-front-a) 0%, var(--photo-front-b) 55%, var(--photo-front-c) 100%);
  }
  .photo-back {
    background:
      radial-gradient(ellipse at 20% 10%, rgba(200,150,150,0.35), transparent 40%),
      linear-gradient(180deg, var(--photo-back-a) 0%, var(--photo-back-b) 50%, var(--photo-back-c) 100%);
  }

  .frame { position: absolute; border: 1px solid var(--frame); }
  .card { position: absolute; background: var(--paper); }

  .logo-frame { left: 85px; top: 305px; width: 308px; height: 110px; }
  .logo-card { left: 93px; top: 313px; width: 292px; height: 95px; display: flex; align-items: center; justify-content: center; }
  .logo-name {
    font-family: "Jost", sans-serif; font-weight: 300; font-size: 38px;
    letter-spacing: 2px; color: var(--ink-logo); text-transform: uppercase;
  }

  .service-frame { width: 193px; height: 192px; }
  .service-card { width: 177px; height: 177px; padding: 33px 12px 0 23px; }
  .col-1 { left: 35px; }
  .col-2 { left: 251px; }
  .col-1.service-card { left: 43px; }
  .col-2.service-card { left: 259px; }
  .row-1 { top: 35px; }
  .row-2 { top: 249px; }
  .row-1.service-card { top: 43px; }
  .row-2.service-card { top: 257px; }

  .service-title {
    font-family: "Jost", sans-serif; font-weight: 400; font-size: 13.5px;
    letter-spacing: 1.8px; line-height: 16.5px; color: var(--ink-heading);
    text-transform: uppercase; margin-left: 2px; margin-bottom: 9px;
  }
  .service-text {
    font-family: "EB Garamond", serif; font-size: 11.2px; line-height: 16px;
    color: var(--ink-body);
  }
</style>
</head>
<body>
<div class="canvas">
  <section class="flyer-side flyer-front">
    <div class="photo photo-front" role="img" aria-label="Transparentes Wohnbild: Holztisch mit Stühlen, Windlichtern und Keramikvasen"></div>
    <div class="frame logo-frame"></div>
    <div class="card logo-card"><span class="logo-name">Heimklang</span></div>
  </section>

  <section class="flyer-side flyer-back">
    <div class="photo photo-back" role="img" aria-label="Blasses Wohnbild im Hintergrund mit Blumen und Holzmöbeln"></div>

    <div class="frame service-frame col-1 row-1"></div>
    <div class="card service-card col-1 row-1">
      <h2 class="service-title">Wohnraum-<br>gestaltung</h2>
      <p class="service-text">Mit der vorhandenen<br>Einrichtung eine Verbesse-<br>rung des Wohngefühls<br>schaffen.</p>
    </div>

    <div class="frame service-frame col-2 row-1"></div>
    <div class="card service-card col-2 row-1">
      <h2 class="service-title">Garten-<br>beratung</h2>
      <p class="service-text">Durch Anregung in der<br>Garten- und Terassen-<br>gestaltung ein neues<br>Erscheinungsbild kreieren.</p>
    </div>

    <div class="frame service-frame col-1 row-2"></div>
    <div class="card service-card col-1 row-2">
      <h2 class="service-title">Raumdesign</h2>
      <p class="service-text">In Praxis- und Gewerberäu-<br>men eine neue Atmosphäre<br>erzielen.</p>
    </div>

    <div class="frame service-frame col-2 row-2"></div>
    <div class="card service-card col-2 row-2">
      <h2 class="service-title">Workshops</h2>
      <p class="service-text">Kreative Gruppenevents<br>zu verschiedensten Anlässen<br>und Themen erleben.</p>
    </div>
  </section>
</div>
</body>
</html>
```